business cards for heating company

I need business cards for my heating air conditioning and chimney company located in upstate NY I would like for them to be colorful and catchy on heavy stock with preferably a glossy finish on front of card but the ability to write something on one half of the back with maybe some bullets on the other half of the back I also need to be able to change the name and title of employees on the card and also incorporate some of our current look and feel from our trucks and website I also want to be able to use this design or similar to have door hangers made lawn signs coffee mugs key chains etc. our website is Brindlecove.com

Target Market(s)

homeowners

Industry/Entity Type

Air Conditioning

Contact Information for Business Card

should have website brindlecove.com , phone number 585-437-9184 please look at website for ideas

Font styles to use
Sans Serif

Colors
ec1f27
3176b5
fbee3f

Requirements
Must have
• a complete look
Nice to have
• a discount offer like 10% military and first responders
• senior discount %5

```html
<!DOCTYPE html>
<html lang="en">
<head>
<meta charset="utf-8">
<title>Brindlecove Business Cards</title>
<link href="https://fonts.googleapis.com/css2?family=Jost:wght@300;400;500;700&display=swap" rel="stylesheet">
<style>
  :root {
    --backdrop: #e9e6e2;
    --rose: #c2435d;
    --rose-dark: #ad3a52;
    --brand-red: #ec1f27;
    --brand-blue: #2a5ea8;
    --brand-yellow: #fbee3f;
    --ink: #2b2b2b;
    --paper: #ffffff;
    --paper-shade: #ececec;
    --accent-red: #c8324a;
  }
  * { box-sizing: border-box; margin: 0; padding: 0; }
  html, body { width: 1200px; height: 904px; overflow: hidden; }
  body {
    background: var(--backdrop);
    font-family: "Jost", Arial, sans-serif;
    position: relative;
  }
  .card {
    position: absolute;
    width: 560px;
    height: 320px;
    box-shadow: 0 10px 24px rgba(0,0,0,.18);
  }
  /* Back card */
  .card-back {
    left: 90px; top: 90px;
    background: radial-gradient(ellipse at 50% 30%, var(--rose) 0%, var(--rose-dark) 100%);
    color: var(--paper);
    text-align: center;
  }
  .card-back .brand { position: absolute; top: 100px; left: 0; right: 0; }
  .brand-name {
    font-weight: 700;
    font-size: 38px;
    letter-spacing: 1px;
    text-transform: uppercase;
    line-height: 1;
  }
  .brand-tagline {
    font-weight: 500;
    font-size: 17px;
    text-transform: uppercase;
    letter-spacing: .5px;
    margin-top: 4px;
  }
  .offers {
    position: absolute; top: 210px; left: 0; right: 0;
    font-weight: 300; font-size: 15px; line-height: 1.35;
  }
  /* Front card */
  .card-front {
    left: 550px; top: 490px;
    background: linear-gradient(135deg, var(--paper) 40%, var(--paper-shade) 100%);
  }
  .edge {
    position: absolute; top: 0; bottom: 0; width: 14px;
    display: flex; flex-direction: column;
  }
  .edge-left { left: 0; }
  .edge-right { right: 0; }
  .edge span { flex: 1; }
  .edge .blue { background: var(--brand-blue); }
  .edge .yellow { background: var(--brand-yellow); }
  .edge .red { background: var(--brand-red); }
  .card-front .brand {
    position: absolute; left: 50px; top: 40px;
    color: var(--accent-red);
  }
  .card-front .brand-name { font-size: 32px; }
  .card-front .brand-tagline { font-size: 14px; }
  .person { position: absolute; right: 52px; top: 56px; text-align: right; }
  .person-name { color: var(--accent-red); font-size: 22px; font-weight: 400; }
  .person-title { color: var(--ink); font-size: 14px; }
  .contact {
    position: absolute; left: 50px; bottom: 30px;
    color: var(--ink); font-size: 16px; line-height: 1.3;
  }
  .address { margin-bottom: 6px; }
  .contact-row { display: flex; align-items: center; gap: 10px; }
  .contact-row svg { width: 16px; height: 16px; fill: var(--brand-blue); flex: none; }
</style>
</head>
<body>
  <section class="card card-back">
    <div class="brand">
      <div class="brand-name">Brindlecove</div>
      <div class="brand-tagline">Heating, Cooling &amp; Chimney</div>
    </div>
    <div class="offers">
      <p>- a discount offer like 10% military and first responders</p>
      <p>- senior discount %5</p>
    </div>
  </section>

  <section class="card card-front">
    <div class="edge edge-left"><span class="blue"></span><span class="yellow"></span><span class="red"></span></div>
    <div class="edge edge-right"><span class="blue"></span><span class="yellow"></span><span class="red"></span></div>

    <div class="brand">
      <div class="brand-name">Brindlecove</div>
      <div class="brand-tagline">Heating, Cooling &amp; Chimney</div>
    </div>

    <div class="person">
      <div class="person-name">Dana Whitfield</div>
      <div class="person-title">Manager</div>
    </div>

    <div class="contact">
      <div class="address">418 Alder Lane<br>Webster, NY 14580</div>
      <div class="contact-row">
        <svg viewBox="0 0 16 16" aria-hidden="true"><path d="M2 4c0-1.5 2.5-2.5 6-2.5s6 1 6 2.5v1.5h-3V4.2C10 3.8 9 3.7 8 3.7s-2 .1-3 .5v1.3H2z M4 7h8l2 7H2z M8 8.5a2 2 0 1 0 0 4a2 2 0 1 0 0-4z"/></svg>
        <span>585-437-9184</span>
      </div>
      <div class="contact-row">
        <svg viewBox="0 0 16 16" aria-hidden="true"><path d="M1 3h14v10H1z M2.5 4.5 8 9l5.5-4.5" stroke="#fff" stroke-width="1"/></svg>
        <span>info@brindlecove.com</span>
      </div>
      <div class="contact-row">
        <svg viewBox="0 0 16 16" aria-hidden="true"><circle cx="8" cy="8" r="7"/><path d="M1 8h14M8 1v14M3 4.5h10M3 11.5h10M8 1c-3 3-3 11 0 14M8 1c3 3 3 11 0 14" stroke="#fff" stroke-width=".8" fill="none"/></svg>
        <span>brindlecove.com</span>
      </div>
    </div>
  </section>
</body>
</html>
```